Cellar Crew Poster / Flyer Ad Design

We need a poster design (and a complimentary A6 flyer) to promote our Adult Rock Band Course called 'Cellar Crew'.

Target market is adults aged 25 - 50 primarily

Design to be eye catching, creative, appealing and easy to understand. Most of the distribution will be street marketing, email marketing, social media, music magazines and websites and to other music teachers.

We need the design to be as an A3 and A4 poster and an A6 promo flyer/e-flyer. Should look good in colour and we'll want a version in black and white.

Would be good to also incorporate our music school logo (just for branding purposes).

Text as follows:

CELLAR CREW
The Ultimate Rock Band Course for Adults

Ever wondered what it would be like to play in a band?

Feeling musically rusty and looking for a way to start playing your instrument again?

Then here’s an exciting opportunity you can’t miss!

All musical levels
Beginner/Intermediate to Advanced Players

Limited Numbers

REGISTER ONLINE NOW
www.tunewellstudio.com.au

Starts Saturday 3rd August
Newtown

Over 6 exciting weekends you’ll work with one of our experienced professional band coaches and transform yourselves into the ultimate ‘Cellar Crew’

Discover how to play in a band
Revisit your musical abilities
Practice songs
Perform on Stage

Drummers, Bass Guitarists, Singers, Keys, Guitarists, Saxophone, Percussionists and others all welcome to join

For more information, course costs and registration, please visit www.tunewellstudio.com.au or call 02 7391 4825 / 0438 572 904

Reason: Hi Everyone, I've been away and unable to respond to some of the designs because I've been ill. Have decided to extend the deadline and now commit to paying designers. Look forward to seeing more designs. Any questions, please let me know. Thanks Melinda

```html
<!DOCTYPE html>
<html lang="en">
<head>
<meta charset="utf-8">
<title>Cellar Crew – Rock Band Course for Adults</title>
<link rel="stylesheet" href="https://fonts.googleapis.com/css2?family=Oswald:wght@400&family=Share+Tech&family=Abel&family=Ubuntu:wght@500&family=Pathway+Gothic+One&display=swap">
<style>
  :root {
    --cream: #ede5c8;
    --orange: #f0552a;
    --teal: #8ee4d0;
    --grey: #6d7779;
    --amber: #f0a02e;
    --ink: #111111;
    --white: #ffffff;
  }
  html, body { margin: 0; padding: 0; overflow: hidden; background: var(--cream); }
  .poster {
    position: relative;
    width: 854px;
    height: 1200px;
    overflow: hidden;
    background: var(--cream);
  }
  .poster > * { position: absolute; margin: 0; white-space: nowrap; line-height: 1; }

  .notes { opacity: .35; border-radius: 20px; }
  .notes--left { left: 18px; top: 20px; width: 50px; height: 320px; background: linear-gradient(180deg, var(--teal), var(--orange), var(--amber)); }
  .notes--right { left: 790px; top: 670px; width: 50px; height: 330px; background: linear-gradient(180deg, var(--amber), var(--grey), var(--orange), var(--teal)); }

  .title { left: 76px; top: 20px; font-family: "Oswald", sans-serif; font-size: 122px; color: var(--orange); letter-spacing: 2px; }
  .subtitle { left: 78px; top: 184px; font-family: "Share Tech", sans-serif; font-size: 35px; color: var(--teal); letter-spacing: .6px; }
  .question { left: 78px; top: 224px; font-family: "Abel", sans-serif; font-size: 30px; color: var(--grey); font-weight: bold; }

  .feeling { left: 70px; top: 355px; transform-origin: left top; transform: rotate(-90deg); font-family: "Abel", sans-serif; font-weight: bold; font-size: 30px; color: var(--grey); }
  .musically { left: 130px; top: 262px; font-family: "Ubuntu", sans-serif; font-size: 50px; color: var(--orange); }
  .rusty { left: 130px; top: 312px; font-family: "Ubuntu", sans-serif; font-size: 58px; color: var(--orange); letter-spacing: 11px; }
  .restart { left: 350px; top: 280px; font-family: "Abel", sans-serif; font-weight: bold; font-size: 31px; color: var(--grey); line-height: 1.5; }

  .opportunity { left: 78px; top: 378px; font-family: "Share Tech", sans-serif; font-size: 25px; color: var(--amber); letter-spacing: .6px; }
  .levels { left: 78px; top: 418px; font-family: "Abel", sans-serif; font-weight: bold; font-size: 50px; color: var(--grey); line-height: 1.1; }

  .starts { left: 78px; top: 540px; font-family: "Ubuntu", sans-serif; font-size: 60px; color: var(--teal); letter-spacing: 14px; }
  .start-date { left: 78px; top: 612px; font-family: "Abel", sans-serif; font-weight: bold; font-size: 42px; color: var(--teal); }
  .start-day { left: 388px; top: 538px; font-family: "Abel", sans-serif; font-weight: bold; font-size: 122px; color: var(--teal); }
  .register {
    left: 538px; top: 545px; width: 126px; height: 126px; border-radius: 50%;
    background: var(--orange); color: var(--white);
    display: flex; align-items: center; justify-content: center; text-align: center;
    font-family: "Pathway Gothic One", sans-serif; font-size: 26px; line-height: 1.05; white-space: normal;
  }
  .limited { left: 740px; top: 662px; transform-origin: left top; transform: rotate(-90deg); font-family: "Pathway Gothic One", sans-serif; font-size: 33px; color: var(--grey); }

  .web { left: 78px; top: 670px; font-family: "Ubuntu", sans-serif; font-size: 46px; color: var(--orange); letter-spacing: 1px; }
  .details { left: 78px; top: 734px; font-family: "Abel", sans-serif; font-weight: bold; font-size: 20.5px; color: var(--grey); line-height: 1.3; }
  .details em { font-style: normal; letter-spacing: 2px; }
  .benefits { left: 78px; top: 801px; font-family: "Pathway Gothic One", sans-serif; font-size: 21px; color: var(--amber); }
  .instruments { left: 78px; top: 832px; font-family: "Share Tech", sans-serif; font-size: 41px; color: var(--teal); line-height: 1.08; }
  .welcome { left: 78px; top: 932px; font-family: "Abel", sans-serif; font-weight: bold; font-size: 30px; color: var(--grey); letter-spacing: 7px; }

  .brand { left: 218px; top: 1030px; display: flex; align-items: center; gap: 34px; }
  .brand-name { font-family: "Share Tech", sans-serif; font-size: 40px; color: var(--teal); }
  .brand-dot { width: 62px; height: 62px; border-radius: 50%; background: var(--orange); }

  .contact { left: 0; width: 854px; top: 1092px; text-align: center; font-family: "Abel", sans-serif; font-weight: bold; font-size: 27px; color: var(--ink); line-height: 1.3; }
</style>
</head>
<body>
<main class="poster">
  <div class="notes notes--left" role="img" aria-label="Scattered music notes"></div>
  <div class="notes notes--right" role="img" aria-label="Scattered music notes"></div>

  <h1 class="title">CELLAR CREW</h1>
  <p class="subtitle">The Ultimate Rock Band Course for Adults</p>
  <p class="question">Ever wondered what it would be like to play in a band?</p>

  <p class="feeling">Feeling</p>
  <p class="musically">musically</p>
  <p class="rusty">rusty</p>
  <p class="restart">and looking for a way to start<br>playing your instrument again?</p>

  <p class="opportunity">Then here’s an exciting opportunity you can’t miss!</p>
  <p class="levels">All musical levels from Beginner/<br>Intermediate to Advanced Players</p>

  <p class="starts">Starts</p>
  <p class="start-date">Saturday August</p>
  <p class="start-day">3rd</p>
  <p class="register">REGISTER<br>ONLINE<br>NOW</p>
  <p class="limited">Limited Numbers</p>

  <p class="web">www.tunewellstudio.com.au</p>
  <p class="details">Over 6 exciting weekends you’ll work with one of our experienced professional<br>band coaches and transform yourselves into the ultimate <em>‘Cellar Crew’</em></p>
  <p class="benefits">Discover how to play in a band, Revisit your musical abilities, Practice songs, Perform on Stage</p>
  <p class="instruments">Drummers, Bass Guitarists, Singers, Keys,<br>Guitarists, Saxophone, Percussionists</p>
  <p class="welcome">and others all welcome to join</p>

  <div class="brand">
    <span class="brand-name">tunewell studio</span>
    <span class="brand-dot"></span>
  </div>

  <p class="contact">For more information, course costs and registration, please visit<br>www.tunewellstudio.com.au or call 02 7391 4825 / 0438 572 904</p>
</main>
</body>
</html>
```